Tasman Curdworks Guild needs new business cards

We need new business cards designed and produced. We are likely to need other design work done for ads, flyers etc in future.

We would like to start with an initial business card.

The Tasman Curdworks Guild (TCG) is a membership-based not-for-profit organisation that looks after the interests of Australia's small to medium artisan cheesemakers, many of whom are also small-scale farmers. The design should be simple, using our logo, but also communicate our artisan cheese and small dairy farm focus.

The first card to be designed and produced is for me, Miriam Tolhurst. My details are:

Miriam Tolhurst
Secretary
Tasman Curdworks Guild (TCG)
http://www.curdworksguild.example
T +61452837190
E miriam.miriamtolhurst@mailbox.example

I have attached the TCG logo in jpg form. I have a higher resolution version available if needed.

Thank you!

Miriam

Miriam Tolhurst
Tasman Curdworks Guild
miriam.miriamtolhurst@mailbox.example
+61452837190

Sans Serif

• Logo (see attached file)

```html
<!DOCTYPE html>
<html lang="en">
<head>
<meta charset="utf-8">
<title>Tasman Curdworks Guild – Business Card</title>
<link rel="stylesheet" href="https://fonts.googleapis.com/css2?family=Open+Sans:wght@400;600;700&display=swap">
<style>
  :root {
    --backdrop: #3b3430;
    --card: #0c0c0c;
    --card-edge: #1c1c1c;
    --gold: #f5c94a;
    --text-light: #e8e8e8;
    --silver: #c9c9c9;
    --divider: #2a2520;
  }
  * { box-sizing: border-box; margin: 0; padding: 0; }
  html, body {
    width: 1200px;
    height: 900px;
    overflow: hidden;
    background: var(--backdrop);
    font-family: "Open Sans", sans-serif;
  }
  .stage {
    position: relative;
    width: 1200px;
    height: 900px;
    display: flex;
    align-items: center;
    justify-content: center;
    gap: 40px;
  }
  .card {
    position: relative;
    width: 520px;
    height: 297px;
    background: var(--card);
    border: 1px solid var(--card-edge);
    box-shadow: 0 10px 30px rgba(0,0,0,0.45);
    overflow: hidden;
  }
  /* Front */
  .card-front .brand {
    position: absolute;
    left: 0;
    top: 0;
    width: 206px;
    height: 100%;
    display: flex;
    flex-direction: column;
    align-items: center;
    justify-content: center;
    gap: 14px;
  }
  .brand-dot {
    width: 64px;
    height: 64px;
    border-radius: 50%;
    background: var(--gold);
  }
  .brand-name {
    color: var(--gold);
    font-weight: 600;
    font-size: 14px;
    text-align: center;
    line-height: 1.3;
  }
  .card-front .divider {
    position: absolute;
    left: 210px;
    top: 80px;
    width: 1px;
    height: 137px;
    background: var(--divider);
  }
  .contact {
    position: absolute;
    left: 226px;
    top: 84px;
    right: 14px;
  }
  .contact-name {
    color: var(--gold);
    font-weight: 700;
    font-size: 19px;
    letter-spacing: 0.3px;
    text-transform: uppercase;
  }
  .contact-role {
    color: var(--text-light);
    font-size: 13px;
    margin-top: 1px;
  }
  .contact-list {
    list-style: none;
    margin-top: 16px;
  }
  .contact-list li {
    display: flex;
    align-items: center;
    gap: 8px;
    color: var(--text-light);
    font-size: 12px;
    line-height: 22px;
    white-space: nowrap;
  }
  .contact-list svg {
    width: 11px;
    height: 11px;
    flex: none;
  }
  /* Back */
  .card-back {
    display: flex;
    align-items: center;
    justify-content: center;
    gap: 18px;
  }
  .card-back .brand-dot {
    background: var(--silver);
    width: 58px;
    height: 58px;
  }
  .card-back .brand-name {
    color: var(--silver);
    font-weight: 400;
    font-size: 22px;
    text-align: left;
    line-height: 1.15;
  }
</style>
</head>
<body>
<main class="stage">
  <section class="card card-front" aria-label="Business card front">
    <div class="brand">
      <span class="brand-dot"></span>
      <span class="brand-name">Tasman Curdworks Guild</span>
    </div>
    <div class="divider"></div>
    <div class="contact">
      <h1 class="contact-name">Miriam Tolhurst</h1>
      <p class="contact-role">Secretary</p>
      <ul class="contact-list">
        <li>
          <svg viewBox="0 0 12 12" aria-hidden="true"><path d="M2.2 1 L4.4 1 L5.2 3.6 L3.9 4.6 Q5 7 7.4 8.1 L8.4 6.8 L11 7.6 L11 9.8 Q10.6 11 9.4 11 Q1 10 1 2.6 Q1 1.4 2.2 1 Z" fill="var(--gold)"/></svg>
          +61452837190
        </li>
        <li>
          <svg viewBox="0 0 12 12" aria-hidden="true"><rect x="0.5" y="2.5" width="11" height="7.5" fill="var(--gold)"/><polyline points="0.8,2.8 6,7 11.2,2.8" fill="none" stroke="var(--card)" stroke-width="1"/></svg>
          miriam.miriamtolhurst@mailbox.example
        </li>
        <li>
          <svg viewBox="0 0 12 12" aria-hidden="true"><circle cx="6" cy="6" r="5.2" fill="var(--gold)"/><ellipse cx="6" cy="6" rx="2.2" ry="5.2" fill="none" stroke="var(--card)" stroke-width="0.8"/><line x1="0.8" y1="6" x2="11.2" y2="6" stroke="var(--card)" stroke-width="0.8"/></svg>
          www.curdworksguild.example
        </li>
      </ul>
    </div>
  </section>

  <section class="card card-back" aria-label="Business card back">
    <span class="brand-dot"></span>
    <span class="brand-name">Tasman<br>Curdworks<br>Guild</span>
  </section>
</main>
</body>
</html>
```